Four in One (Flexible infographic for Content Management Industry)

See attachment.
A graphic depicting 4 products, where each can stand on its own and each can be combined with others, but where, if all are taken together, the best result is achieved (the "super product").
Intended use is web. See attached file as an example.
The most basic idea is as the attached diagram shows, where 4 rectangles are arranged in a quadrangle, with a middle rectangle in the center representing the combined 4 products. This concept is fine except it is a bit too obvious as it stands. We are looking for either a variation of this or another concept.
The audience is technical + professional + enterprise - NOT consumers. Hence the design should be conservative in nature.
We are aware of tools like as Canva or Pictogram where such graphics are available, but we are looking for something with a bit more imagination and flexibility.
This graphic should be targeted to web sites and be delivered with vector-based (SVG) graphics.

```html
<!DOCTYPE html>
<html lang="en">
<head>
<meta charset="utf-8">
<title>Four in One – Super Product</title>
<link rel="stylesheet" href="https://fonts.googleapis.com/css2?family=Montserrat:wght@400;500;600;700&display=swap">
<style>
  :root {
    --blue: #1d7a9a;
    --yellow: #e3b022;
    --teal: #139681;
    --green: #9dc13c;
    --purple: #9c4592;
    --white: #ffffff;
    --page: #ffffff;
  }
  * { margin: 0; padding: 0; box-sizing: border-box; }
  html, body { width: 1200px; height: 675px; overflow: hidden; background: var(--page); }
  body { font-family: "Montserrat", Arial, sans-serif; color: var(--white); }
  .canvas { position: relative; width: 1200px; height: 675px; overflow: hidden; }
  .diagram { position: absolute; inset: 0; width: 1200px; height: 675px; }

  .hub-title {
    position: absolute; left: 494px; top: 321px; width: 212px;
    text-align: center; font-weight: 700; font-size: 20px; letter-spacing: 0.2px;
  }

  .card { position: absolute; width: 148px; }
  .card h2 { font-size: 7.6px; font-weight: 700; margin-bottom: 3.5px; }
  .card p { font-size: 5.9px; line-height: 7.1px; margin-bottom: 3px; }
  .card ul { list-style: none; }
  .card li { font-size: 5.9px; line-height: 10.3px; }
  .card li::before { content: "· "; }
  .card .learn { display: inline-block; margin-top: 1px; font-size: 7px; font-weight: 600; color: var(--white); text-decoration: none; }
  .card .learn::after { content: " ▸"; font-size: 5px; }

  .card--security { left: 529px; top: 58px; }
  .card--documents { left: 289px; top: 298px; }
  .card--digital { left: 771px; top: 298px; }
  .card--erp { left: 526px; top: 535px; }

  .icon { position: absolute; }
  .icon--cloud { left: 576px; top: 190px; width: 48px; height: 33px; }
  .icon--doc { left: 450px; top: 314px; width: 36px; height: 47px; }
  .icon--search { left: 715px; top: 314px; width: 46px; height: 47px; }
  .icon--apps { left: 576px; top: 449px; width: 48px; height: 48px; }
</style>
</head>
<body>
<main class="canvas">
  <svg class="diagram" viewBox="0 0 1920 1080" aria-hidden="true">
    <defs>
      <path id="petal" d="M 845 430 C 870 390 878 370 873 345 C 865 290 790 220 790 160 C 790 80 870 17 960 17 C 1050 17 1130 80 1130 160 C 1130 220 1055 290 1047 345 C 1042 370 1050 390 1075 430 L 960 540 Z"/>
    </defs>
    <use href="#petal" fill="var(--blue)"/>
    <use href="#petal" fill="var(--teal)" transform="rotate(90 960 540)"/>
    <use href="#petal" fill="var(--green)" transform="rotate(180 960 540)"/>
    <use href="#petal" fill="var(--yellow)" transform="rotate(270 960 540)"/>
    <path class="hub" fill="var(--purple)" d="M 910 392 Q 960 360 1010 392 L 1080 437 Q 1130 470 1130 540 Q 1130 610 1080 643 L 1010 688 Q 960 720 910 688 L 840 643 Q 790 610 790 540 Q 790 470 840 437 Z"/>
  </svg>

  <div class="hub-title">Super Product</div>

  <svg class="icon icon--cloud" viewBox="0 0 48 33" aria-hidden="true">
    <path fill="var(--white)" d="M10 33 C4 33 0 29 0 24 C0 19 4 15 9 15 C10 7 16 0 24 0 C31 0 36 5 37 11 C43 11 48 16 48 22 C48 28 43 33 38 33 Z"/>
    <path fill="none" stroke="var(--blue)" stroke-width="3.6" stroke-linecap="round" stroke-linejoin="round" d="M16 20 L22 26 L32 13"/>
  </svg>

  <svg class="icon icon--doc" viewBox="0 0 36 47" aria-hidden="true">
    <path fill="var(--white)" d="M3 0 H22 V11 C22 13 23 14 25 14 H36 V44 C36 46 35 47 33 47 H3 C1 47 0 46 0 44 V3 C0 1 1 0 3 0 Z"/>
    <path fill="var(--white)" d="M25 0 L36 11 H26 C25.4 11 25 10.6 25 10 Z"/>
    <g stroke="var(--yellow)" stroke-width="2.4" stroke-linecap="round">
      <line x1="7" y1="20" x2="22" y2="20"/>
      <line x1="7" y1="27" x2="29" y2="27"/>
      <line x1="7" y1="34" x2="29" y2="34"/>
      <line x1="7" y1="41" x2="15" y2="41"/>
    </g>
  </svg>

  <svg class="icon icon--search" viewBox="0 0 46 47" aria-hidden="true">
    <rect width="46" height="47" rx="6" fill="var(--white)"/>
    <circle cx="20" cy="20" r="10" fill="none" stroke="var(--teal)" stroke-width="4"/>
    <line x1="27.5" y1="27.5" x2="35" y2="35" stroke="var(--teal)" stroke-width="5" stroke-linecap="round"/>
  </svg>

  <svg class="icon icon--apps" viewBox="0 0 48 48" aria-hidden="true">
    <g fill="var(--white)">
      <rect x="0" y="3" width="21" height="21" rx="4"/>
      <rect x="0" y="27" width="21" height="21" rx="4"/>
      <rect x="25" y="27" width="21" height="21" rx="4"/>
      <rect x="26" y="2" width="18" height="18" rx="4" transform="rotate(45 35 11)"/>
    </g>
  </svg>

  <section class="card card--security">
    <h2>Security and Compliance</h2>
    <p>Benefit from tailored cloud solutions, secure data storage, and expert disaster recovery planning for reliable and scalable IT operations.</p>
    <ul>
      <li>Custom Cloud Solutions</li>
      <li>Secure Data Storage</li>
      <li>Expert Disaster Recovery</li>
    </ul>
    <a class="learn" href="#">Learn More</a>
  </section>

  <section class="card card--documents">
    <h2>Document Management</h2>
    <p>Streamline document organization, access, and collaboration with easier file storage and sharing, leading to more efficient workflows.</p>
    <ul>
      <li>Centralized Document Control</li>
      <li>Collaborative Workspace Integration</li>
      <li>Automated Compliance Tracking</li>
    </ul>
    <a class="learn" href="#">Learn More</a>
  </section>

  <section class="card card--digital">
    <h2>Digitital Transformation</h2>
    <p>Turn scanned documents into easily searchable digital archives, boosting efficiency and accessibility.</p>
    <ul>
      <li>Instant searchable Archives with OCR</li>
      <li>Automated Document Classification</li>
      <li>TeamVault and Cloud Blob Ready</li>
    </ul>
    <a class="learn" href="#">Learn More</a>
  </section>

  <section class="card card--erp">
    <h2>Enterprise Resource Planning</h2>
    <p>Simplify management across finance, sales, and operations, enabling better decision-making and improved productivity.</p>
    <ul>
      <li>Integrated Business Processes</li>
      <li>Enhanced Decision-Making</li>
      <li>Productivity Improvement</li>
    </ul>
    <a class="learn" href="#">Learn More</a>
  </section>
</main>
</body>
</html>
```